Talvenridge

We are re-branding the company with a new logo (attached) which I would
like to go on one side of the card, and I have attached a file showing what
the old back side looked like, and I do like the characters that show the
phone, e-mails, etc., I don't like the current arrangement, and I want
something clean, clear and out of the box, as we are an aviation consulting
firm, and we work outside of the box.

```html
<!DOCTYPE html>
<html lang="en">
<head>
<meta charset="utf-8">
<title>Talvenridge – Business Card</title>
<link rel="stylesheet" href="https://fonts.googleapis.com/css2?family=Quicksand:wght@400;500;600&display=swap">
<style>
  :root {
    --backdrop-light: #f7f7f7;
    --backdrop-dark: #cfcfcf;
    --card-white: #ffffff;
    --card-charcoal: #4a4643;
    --brand-red: #bd1a1a;
    --ink-dark: #3b3b3b;
    --ink-grey: #8a8a8a;
    --text-light: #ffffff;
  }
  * { margin: 0; padding: 0; box-sizing: border-box; }
  html, body {
    width: 1200px;
    height: 900px;
    overflow: hidden;
  }
  body {
    position: relative;
    font-family: "Quicksand", sans-serif;
    background: radial-gradient(ellipse at 50% 40%, var(--backdrop-light) 0%, #e6e6e6 55%, var(--backdrop-dark) 100%);
  }
  .card {
    position: absolute;
    top: 302px;
    width: 543px;
    height: 302px;
    overflow: hidden;
    box-shadow: 0 2px 6px rgba(0,0,0,0.12);
  }

  /* Front */
  .card-front {
    left: 43px;
    background: var(--card-white);
    border-top-left-radius: 92px;
  }
  .brand {
    position: absolute;
    left: 45px;
    top: 100px;
  }
  .brand-name {
    display: flex;
    align-items: center;
    gap: 12px;
    font-size: 36px;
    font-weight: 600;
    letter-spacing: 1px;
    color: var(--ink-dark);
    line-height: 1;
  }
  .brand-dot {
    width: 22px;
    height: 22px;
    border-radius: 50%;
    background: var(--brand-red);
  }
  .brand-tagline {
    margin-top: 8px;
    margin-left: 40px;
    font-size: 11px;
    color: var(--ink-grey);
    letter-spacing: 0.5px;
  }
  .brand-tagline .sep { color: var(--brand-red); }
  .services-band {
    position: absolute;
    left: 0;
    bottom: 0;
    width: 100%;
    height: 37px;
    padding: 0 12px;
    background: var(--brand-red);
    display: flex;
    align-items: center;
    justify-content: center;
    gap: 7px;
    color: var(--text-light);
    font-size: 12.5px;
    font-weight: 500;
    letter-spacing: -0.4px;
    list-style: none;
  }
  .service-item {
    flex: none;
    white-space: nowrap;
  }

  /* Back */
  .card-back {
    left: 623px;
    background: var(--card-charcoal);
    border-top-right-radius: 92px;
  }
  .accent-band {
    position: absolute;
    left: 0;
    bottom: 0;
    width: 100%;
    height: 21px;
    background: var(--brand-red);
  }
  .person {
    position: absolute;
    right: 288px;
    top: 146px;
    text-align: right;
    color: var(--text-light);
  }
  .person-name {
    font-size: 24px;
    font-weight: 500;
    letter-spacing: -0.3px;
    line-height: 1.1;
  }
  .person-title {
    font-size: 15px;
    font-weight: 500;
    margin-top: 2px;
  }
  .contact-list {
    position: absolute;
    left: 304px;
    top: 88px;
    list-style: none;
    color: var(--text-light);
    font-size: 16px;
    font-weight: 500;
  }
  .contact-item {
    display: flex;
    align-items: center;
    gap: 10px;
    height: 29px;
  }
  .contact-item.address {
    height: 44px;
    line-height: 1.2;
    margin-bottom: 18px;
  }
  .contact-icon {
    width: 16px;
    height: 16px;
    flex: none;
    fill: none;
    stroke: var(--text-light);
    stroke-width: 1.5;
  }
</style>
</head>
<body>

<section class="card card-front">
  <div class="brand">
    <div class="brand-name"><span class="brand-dot"></span>Talvenridge</div>
    <p class="brand-tagline">trusted experience <span class="sep">&bull;</span> proven solutions</p>
  </div>
  <ul class="services-band">
    <li class="service-item">&bull;Aircraft finance/leasing</li>
    <li class="service-item">&bull;Technical services</li>
    <li class="service-item">&bull;Aviation consulting</li>
    <li class="service-item">&bull;Airline restructuring</li>
  </ul>
</section>

<section class="card card-back">
  <div class="person">
    <p class="person-name">Marcus D. Ellery</p>
    <p class="person-title">President &amp; CEO</p>
  </div>

  <ul class="contact-list">
    <li class="contact-item address">
      <svg class="contact-icon" viewBox="0 0 16 16"><path d="M8 15s-5-5.2-5-8.6A5 5 0 0 1 13 6.4C13 9.8 8 15 8 15z" fill="#fff" stroke="none"/><circle cx="8" cy="6.3" r="1.9" fill="#4a4643" stroke="none"/></svg>
      <span>2741B Juniper Hollow<br>Redfield, CA 92418</span>
    </li>
    <li class="contact-item">
      <svg class="contact-icon" viewBox="0 0 16 16"><circle cx="8" cy="8" r="6.5"/><ellipse cx="8" cy="8" rx="2.8" ry="6.5"/><path d="M1.5 8h13M2.5 4.8h11M2.5 11.2h11"/></svg>
      <span>www.tvr.aero</span>
    </li>
    <li class="contact-item">
      <svg class="contact-icon" viewBox="0 0 16 16"><rect x="4" y="1.5" width="8" height="13" rx="1.5" transform="rotate(30 8 8)"/><path d="M6.5 11.5l2 1.2"/></svg>
      <span>+1 480 555 0147</span>
    </li>
    <li class="contact-item">
      <svg class="contact-icon" viewBox="0 0 16 16"><path d="M1.5 6c0-2 3-3 6.5-3s6.5 1 6.5 3l-2.5.5-.5-1.5h-7l-.5 1.5z" fill="#fff"/><path d="M3.5 7.5h9l1 6h-11z" fill="#fff"/><circle cx="8" cy="10.5" r="1.5" fill="#4a4643" stroke="none"/></svg>
      <span>+1 951 555 0182</span>
    </li>
    <li class="contact-item">
      <svg class="contact-icon" viewBox="0 0 16 16"><rect x="1.5" y="3.5" width="13" height="9"/><path d="M1.5 3.5L8 9l6.5-5.5M1.5 12.5l5-4.5M14.5 12.5l-5-4.5"/></svg>
      <span>md@tvr.aero</span>
    </li>
  </ul>

  <div class="accent-band"></div>
</section>

</body>
</html>
```